Business Card Design

New business card design

Target Market(s)

Residential & Commercial Property Managers

Industry/Entity Type

Plumbing Services

Contact Information for Business Card

Name - Owen Tredgold, title - Director, Phone Number - 0431 862 507, email - owen@rvb-plumbing.com.au, Company ABN - 73 215 904 386,

Font styles to use
Sans Serif

Colors
0054AA
0677BA
7BADD7
CADEEF
E8F1F8

```html
<!DOCTYPE html>
<html lang="en">
<head>
<meta charset="UTF-8">
<title>RVB Plumbing Services – Business Card</title>
<link rel="stylesheet" href="https://fonts.googleapis.com/css2?family=Lato:wght@300;400;700;900&display=swap">
<style>
  :root {
    --backdrop: #2a2b2d;
    --backdrop-edge: #161718;
    --card: #1e232a;
    --accent: #08a5e6;
    --ink: #ffffff;
    --ink-soft: #c9cdd2;
    --tagline: #9aa1a8;
  }
  * { margin: 0; padding: 0; box-sizing: border-box; }
  html, body { width: 1200px; height: 952px; overflow: hidden; }
  body {
    background: radial-gradient(ellipse at 55% 50%, var(--backdrop) 0%, var(--backdrop-edge) 80%);
    font-family: "Lato", sans-serif;
    position: relative;
  }
  .card {
    position: absolute;
    width: 580px;
    height: 331px;
    background: var(--card);
    border-radius: 4px;
    overflow: hidden;
    box-shadow: 0 18px 40px rgba(0,0,0,.55);
  }
  .card--front { left: 310px; top: 90px; }
  .card--back { left: 310px; top: 530px; }

  .tab {
    position: absolute;
    background: var(--accent);
  }
  .card--front .tab--top { left: 36px; top: 0; width: 150px; height: 34px; border-radius: 0 0 8px 8px; }
  .card--front .tab--bottom { right: 36px; bottom: 0; width: 150px; height: 34px; border-radius: 8px 8px 0 0; }

  .brand {
    position: absolute;
    text-align: center;
    color: var(--ink);
  }
  .brand__name {
    display: block;
    font-weight: 300;
    letter-spacing: 4px;
    line-height: 1;
  }
  .brand__tagline {
    display: block;
    font-weight: 300;
    color: var(--tagline);
    text-transform: lowercase;
  }
  .card--front .brand { left: 0; right: 0; top: 100px; }
  .card--front .brand__name { font-size: 96px; }
  .card--front .brand__tagline { font-size: 12px; letter-spacing: 9px; margin-top: 10px; }

  .card--back .brand { left: 150px; top: 24px; width: 260px; }
  .card--back .brand__name { font-size: 62px; }
  .card--back .brand__tagline { font-size: 9px; letter-spacing: 7px; margin-top: 6px; }

  .contact {
    position: absolute;
    left: 48px;
    top: 140px;
    color: var(--ink);
  }
  .contact__name {
    font-weight: 900;
    font-size: 22px;
    color: var(--accent);
    text-transform: uppercase;
    letter-spacing: .5px;
  }
  .contact__title { font-size: 14px; color: var(--ink-soft); margin: 2px 0 10px; }
  .contact__line {
    display: flex;
    align-items: center;
    gap: 10px;
    font-size: 15px;
    margin-bottom: 6px;
  }
  .contact__icon {
    width: 18px; height: 18px;
    background: var(--accent);
    border-radius: 3px;
    display: flex; align-items: center; justify-content: center;
  }
  .abn-band {
    position: absolute;
    left: 0;
    bottom: 42px;
    width: 330px;
    height: 34px;
    background: var(--accent);
    clip-path: polygon(0 0, 100% 0, 96% 100%, 0 100%);
    color: var(--ink);
    font-size: 15px;
    display: flex;
    align-items: center;
    padding-left: 48px;
    letter-spacing: .5px;
  }
  .card--back .tab--corner { right: 0; bottom: 0; width: 120px; height: 26px; border-radius: 6px 0 0 0; }
</style>
</head>
<body>

  <section class="card card--front" aria-label="Business card front">
    <div class="tab tab--top"></div>
    <div class="brand">
      <span class="brand__name">rvb</span>
      <span class="brand__tagline">plumbing services</span>
    </div>
    <div class="tab tab--bottom"></div>
  </section>

  <section class="card card--back" aria-label="Business card back">
    <div class="brand">
      <span class="brand__name">rvb</span>
      <span class="brand__tagline">plumbing services</span>
    </div>
    <div class="contact">
      <p class="contact__name">Owen Tredgold</p>
      <p class="contact__title">Director</p>
      <p class="contact__line">
        <span class="contact__icon">
          <svg width="12" height="12" viewBox="0 0 24 24" aria-hidden="true"><path fill="#fff" d="M6.6 10.8a15.1 15.1 0 0 0 6.6 6.6l2.2-2.2a1 1 0 0 1 1-.25 11.4 11.4 0 0 0 3.6.57 1 1 0 0 1 1 1V20a1 1 0 0 1-1 1A17 17 0 0 1 3 4a1 1 0 0 1 1-1h3.5a1 1 0 0 1 1 1c0 1.25.2 2.45.57 3.57a1 1 0 0 1-.25 1z"/></svg>
        </span>
        0431 862 507
      </p>
      <p class="contact__line">
        <span class="contact__icon">
          <svg width="12" height="12" viewBox="0 0 24 24" aria-hidden="true"><path fill="none" stroke="#fff" stroke-width="2.4" d="M3 6h18v12H3zM3 6l9 7 9-7"/></svg>
        </span>
        owen@rvb-plumbing.com.au
      </p>
    </div>
    <div class="abn-band">ABN - 73 215 904 386</div>
    <div class="tab tab--corner"></div>
  </section>

</body>
</html>
```